Computer consultant business card

Plimvo Software is a newly started computer consulting company. It's a small one-man company that provides mostly Android applications but also websites in collaboration with designers. I'm running this company on the side of full time university studies.

I want the final design to be clean and memorable. Be creative! :)

Some inspiration:
http://www.artfenwick.com/design/62242
http://www.artfenwick.com/design/1628455/business-card-design-by-brusqlin
http://www.artfenwick.com/design/918507/business-card-design-by-velinora-quathbridge

See attachment for my company logo.
Updates

I would like to thank everyone for submitting! I'll need a couple of days to review and ultimately select a design.

Target Market(s)

Non-technical entrepreneurs and small companies.

Industry/Entity Type

University

Requirements
Must have
• My company logo.
In any way, both colors from my logo.
First- and last name, e-mail and phone number.
Double-sided design.
Nice to have
• Something creative with the symbol in my logo

```html
<!DOCTYPE html>
<html lang="en">
<head>
<meta charset="utf-8">
<title>Plimvo Software – Business Card</title>
<link rel="stylesheet" href="https://fonts.googleapis.com/css2?family=Exo+2:wght@400;600&display=swap">
<style>
  :root {
    --backdrop: #2b2b2b;
    --card-dark: #3a3a3a;
    --card-dark-edge: #2e2e2e;
    --card-light: #ffffff;
    --card-light-edge: #c9cbd0;
    --brand-blue: #4a7bd0;
    --brand-charcoal: #2f2f2f;
    --text-light: #e4e4e4;
    --divider: #8a8a8a;
  }
  * { box-sizing: border-box; margin: 0; padding: 0; }
  html, body {
    width: 1200px; height: 720px; overflow: hidden;
    background: var(--backdrop);
    font-family: "Exo 2", sans-serif;
  }
  .canvas {
    position: relative; width: 1200px; height: 720px;
  }
  .card {
    position: absolute; top: 204px;
    width: 520px; height: 312px;
    border-radius: 3px;
    box-shadow: 0 10px 30px rgba(0,0,0,0.5);
  }
  .card-front {
    left: 60px;
    background: radial-gradient(ellipse at 40% 45%, var(--card-dark) 0%, var(--card-dark-edge) 100%);
  }
  .card-back {
    left: 620px;
    background: radial-gradient(ellipse at 50% 40%, var(--card-light) 30%, var(--card-light-edge) 100%);
  }
  .brand-dot {
    position: absolute; border-radius: 50%;
  }
  .card-front .brand-dot {
    left: 94px; top: 126px; width: 60px; height: 60px;
    background: var(--brand-blue);
  }
  .divider {
    position: absolute; left: 215px; top: 108px;
    width: 2px; height: 96px;
    background: var(--divider);
  }
  .contact {
    position: absolute; left: 240px; top: 118px;
    color: var(--text-light);
    line-height: 1.45;
  }
  .contact .name { font-size: 18px; font-weight: 400; }
  .contact .first-name { color: var(--brand-blue); }
  .contact .email { font-size: 16px; }
  .contact .phone { font-size: 16px; color: var(--brand-blue); }
  .wordmark {
    position: absolute; left: 0; right: 0; top: 0; bottom: 0;
    display: flex; align-items: center; justify-content: center; gap: 18px;
  }
  .card-back .brand-dot {
    position: static; width: 58px; height: 58px;
    background: var(--brand-charcoal);
  }
  .wordmark-name {
    font-size: 64px; font-weight: 600;
    color: var(--brand-charcoal);
    letter-spacing: 1px;
  }
</style>
</head>
<body>
  <main class="canvas">
    <section class="card card-front" aria-label="Card front">
      <span class="brand-dot"></span>
      <span class="divider"></span>
      <div class="contact">
        <p class="name"><span class="first-name">Marten</span> Velloq Arbison</p>
        <p class="email">MartenVelloq@plimvo.com</p>
        <p class="phone">615-208-473</p>
      </div>
    </section>
    <section class="card card-back" aria-label="Card back">
      <div class="wordmark">
        <span class="brand-dot"></span>
        <span class="wordmark-name">plimvo</span>
      </div>
    </section>
  </main>
</body>
</html>
```